Website for business consultancy - bright and happy feel needed

I need a website with 3/4 pages. I want the first page designed first and the rest will be easy. I need some pictures but none with corporate looking people. I need links to quillpost and deskroster. I need a contact form. I have samples of websites i like, fonts i like and I need a small logo also. I like simple, clean lines and I want a bright, happy and feminine feel. My audience are small businesses so I don't want them intimidated by new much of a corporate feel.
Updates

Target Market(s)

Small medium size businesses who want to grow and need that help but they cannot afford a full time financial director.

Industry/Entity Type

Business Consultant

Number of Pages Required

4 page

Other font styles liked:
• i can attach images

Colors
fcf0f6
e667a6
85cae6
ffffff
fbee3e

Requirements
Must have
• Link to quillpost and desk roster
• Contact form linked to my email
• Pictures - full width images where required
• Colour
• Mobile ready
• Soft feminine feel to it
• I dont want it to look like a corporate business consultancy - much more marketing or interior deign feel
Nice to have
• I would like the 3 services I have in 3 boxes that you click and takes you to a place with more information on the service.
• pictures thinking outside of the box
• Can be wordpress if need be
Should not have
• pictures with too much of a corporate feel
• No pictures of coporate people at all
• i like the following websites
• www.marbelquint.co.uk and others that are attached in the documents with a feminine feel to them

```html
<!DOCTYPE html>
<html lang="en">
<head>
<meta charset="utf-8">
<title>Maren Holt Consultancy</title>
<link rel="stylesheet" href="https://fonts.googleapis.com/css2?family=Questrial&family=Kumbh+Sans:wght@600;700&family=Open+Sans:wght@400&display=swap">
<style>
  :root {
    --white: #ffffff;
    --blush: #fcf0f6;
    --rose: #e667a6;
    --rose-deep: #c94a8a;
    --sky: #85cae6;
    --sun: #fbee3e;
    --ink: #2b1a24;
    --tile-fill: rgba(230, 103, 166, 0.80);
    --tile-frame: #e667a6;
    --tile-inner: #ffffff;
    --footer-dark: #4f2a42;
    --field: #fcf0f6;
    --field-text: #8a6a7c;
  }
  * { box-sizing: border-box; margin: 0; padding: 0; }
  html, body { width: 1200px; height: 738px; overflow: hidden; background: var(--white); }
  body { position: relative; font-family: "Questrial", sans-serif; color: var(--ink); }

  .site-header { position: absolute; left: 0; top: 0; width: 1200px; height: 106px; background: var(--white); }
  .brand-name {
    position: absolute; left: 0; top: 36px; width: 1200px; text-align: center; line-height: 40px;
    font-family: "Questrial", sans-serif; font-weight: 400; font-size: 34px; letter-spacing: 1px; color: var(--ink);
  }

  .main-nav { position: absolute; left: 0; top: 106px; width: 1200px; height: 44px; background: var(--rose); }
  .nav-link {
    position: absolute; top: 12px; font-family: "Kumbh Sans", sans-serif; font-weight: 700;
    font-size: 17px; letter-spacing: 0.4px; color: var(--white); text-decoration: none; line-height: 20px;
  }
  .nav-link.is-active::after {
    content: ""; position: absolute; left: -1px; right: -1px; top: 27px; height: 4px; background: var(--sun);
  }

  .hero { position: absolute; left: 0; top: 150px; width: 1200px; height: 410px; }
  .hero-photo {
    position: absolute; inset: 0;
    background:
      radial-gradient(ellipse at 15% 60%, rgba(230,103,166,0.30), transparent 48%),
      radial-gradient(ellipse at 88% 40%, rgba(133,202,230,0.55), transparent 45%),
      radial-gradient(ellipse at 55% 85%, rgba(251,238,62,0.25), transparent 40%),
      linear-gradient(180deg, #f7dbe9 0%, #eed9e6 50%, #cfe8f3 100%);
  }
  .tagline-band {
    position: absolute; left: 0; top: 0; width: 1200px; height: 48px; background: rgba(252, 240, 246, 0.95);
    text-align: center; font-size: 24px; line-height: 48px; letter-spacing: 0.3px; color: var(--ink);
  }
  .service-tile {
    position: absolute; top: 106px; width: 282px; height: 249px;
    border: 2px solid var(--tile-frame); padding: 5px; text-decoration: none;
  }
  .service-tile.tone-sky { border-color: var(--sky); }
  .service-tile-inner {
    width: 100%; height: 100%; border: 3px solid var(--tile-inner); background: var(--tile-fill);
    display: flex; align-items: center; justify-content: center; padding-bottom: 4px;
    font-family: "Kumbh Sans", sans-serif; font-weight: 600; font-size: 27px; line-height: 28px;
    color: var(--white); text-align: center;
  }
  .tone-sky .service-tile-inner { background: rgba(133, 202, 230, 0.88); }

  .site-footer { position: absolute; left: 0; top: 560px; width: 1200px; height: 178px; background: var(--footer-dark); }
  .footer-title {
    position: absolute; left: 60px; top: 22px; font-family: "Kumbh Sans", sans-serif; font-weight: 600;
    font-size: 20px; color: var(--white);
  }
  .contact-form .field {
    position: absolute; width: 194px; height: 37px; background: var(--field); border: none; outline: none;
    font-family: "Open Sans", sans-serif; font-size: 13px; color: var(--field-text); padding: 0 8px;
  }
  .contact-form .field::placeholder { color: var(--field-text); }
  .contact-form .field-message { height: 80px; padding: 8px; resize: none; }
  .submit-button {
    position: absolute; left: 657px; top: 103px; width: 108px; height: 36px; border: none;
    background: var(--rose); color: var(--white); font-family: "Kumbh Sans", sans-serif;
    font-weight: 600; font-size: 20px;
  }
  .copyright {
    position: absolute; left: 798px; top: 117px; font-family: "Open Sans", sans-serif;
    font-size: 13.5px; color: var(--white);
  }
</style>
</head>
<body>
  <header class="site-header">
    <h1 class="brand-name">MAREN HOLT CONSULTANCY</h1>
  </header>

  <nav class="main-nav">
    <a class="nav-link is-active" href="#" style="left:293px">MEETING</a>
    <a class="nav-link" href="#" style="left:431px">FINANCE</a>
    <a class="nav-link" href="#" style="left:580px">MAREN HOLT KEY</a>
    <a class="nav-link" href="#" style="left:800px">CONTACT US</a>
  </nav>

  <section class="hero">
    <div class="hero-photo" role="img" aria-label="Softly blurred photo of a small team talking around a table"></div>
    <p class="tagline-band">Not all business a afford the Divide</p>
    <a class="service-tile" href="#" style="left:62px"><span class="service-tile-inner">Business concern<br>and Mentor</span></a>
    <a class="service-tile tone-sky" href="#" style="left:437px"><span class="service-tile-inner">Business concern<br>and Mentor</span></a>
    <a class="service-tile" href="#" style="left:812px"><span class="service-tile-inner">Business concern<br>and Mentor</span></a>
  </section>

  <footer class="site-footer">
    <h2 class="footer-title">Contact us</h2>
    <form class="contact-form">
      <input class="field" type="text" placeholder="Name" style="left:60px;top:60px">
      <input class="field" type="email" placeholder="Email id" style="left:259px;top:60px">
      <textarea class="field field-message" placeholder="Message" style="left:458px;top:60px"></textarea>
      <input class="field" type="tel" placeholder="Phone no" style="left:60px;top:103px">
      <input class="field" type="text" placeholder="Location" style="left:259px;top:103px">
      <button class="submit-button" type="button">Submit</button>
    </form>
    <p class="copyright">Copyright © MarenHoltConsultancy All rights reserved.</p>
  </footer>
</body>
</html>
```